Home Security Company Business Card

Looking for a eye catching business card that is non traditional and stands out but yet still looks professional. It should include all the pertinent information such as name, title, address, telephone, e-mail, website address should definitely stand out and then finally the logo.

Target Market(s)

Residential and Commercial accounts mostly upscale accounts

Industry/Entity Type

Security

Contact Information for Business Card

Name
Title
Address
Office #
Cell #
E-mail
Website

Font styles to use
Serif
Sans Serif

Requirements
Must have
• Logo, two sided color configuration
Nice to have
• You decide
Should not have
• There really aren't any.

```html
<!DOCTYPE html>
<html lang="en">
<head>
<meta charset="utf-8">
<title>Harborline Security Systems – Business Card</title>
<link rel="stylesheet" href="https://fonts.googleapis.com/css2?family=Source+Sans+3:wght@300;400;600;700&display=swap">
<style>
  :root {
    --backdrop: #e9e4dc;
    --card: #ffffff;
    --card-shade: #f2f2f2;
    --brand-red: #a8192a;
    --brand-red-dark: #8a1020;
    --gold: #e9b63c;
    --text-grey: #6b6b6b;
    --text-dark: #4a4a4a;
  }
  * { box-sizing: border-box; margin: 0; padding: 0; }
  html, body { width: 1200px; height: 973px; overflow: hidden; }
  body {
    background: var(--backdrop);
    font-family: "Source Sans 3", "Helvetica Neue", Arial, sans-serif;
    position: relative;
  }
  .card {
    position: absolute;
    width: 560px;
    height: 320px;
    border-radius: 16px;
    background: linear-gradient(160deg, var(--card) 55%, var(--card-shade));
    box-shadow: 0 10px 28px rgba(60, 40, 20, 0.25);
    overflow: hidden;
  }
  .card--front { left: 60px; top: 110px; }
  .card--back { left: 580px; top: 540px; }

  /* Front */
  .brand {
    position: absolute;
    left: 40px;
    top: 44px;
    display: flex;
    align-items: center;
    gap: 10px;
  }
  .brand__dot {
    width: 14px; height: 14px; border-radius: 50%;
    background: var(--brand-red);
  }
  .brand__name {
    color: var(--brand-red);
    font-weight: 600;
    font-size: 20px;
    letter-spacing: 0.04em;
    line-height: 1.05;
  }
  .brand__name small { display: block; font-size: 10px; letter-spacing: 0.08em; }

  .person { position: absolute; left: 40px; top: 126px; }
  .person__name {
    color: var(--brand-red);
    font-weight: 700;
    font-size: 25px;
    line-height: 1;
  }
  .person__title {
    color: var(--text-dark);
    font-weight: 300;
    font-size: 17px;
    margin-top: 2px;
  }

  .contacts { position: absolute; left: 40px; top: 190px; list-style: none; }
  .contacts li {
    display: flex; align-items: center; gap: 10px;
    color: var(--text-grey);
    font-weight: 300;
    font-size: 15px;
    height: 22px;
  }
  .icon { width: 12px; height: 12px; fill: var(--brand-red); flex: none; }

  .address {
    position: absolute; right: 28px; bottom: 12px;
    height: 22px;
    display: flex; align-items: center; gap: 8px;
    color: var(--text-grey); font-weight: 300; font-size: 15px;
  }

  .web-band {
    position: absolute; left: 0; bottom: 0; width: 290px; height: 42px;
    border-top-right-radius: 14px;
    background: linear-gradient(180deg, var(--brand-red), var(--brand-red-dark));
    display: flex; align-items: center; gap: 10px;
    padding-left: 40px;
    color: #fff; font-size: 17px; font-weight: 400;
  }
  .web-band .icon { fill: #fff; width: 15px; height: 15px; }

  /* Back */
  .card--back .edge {
    position: absolute; left: 0; top: 0; bottom: 0; width: 12px;
    background: linear-gradient(90deg, var(--brand-red), var(--gold));
  }
  .back-brand {
    position: absolute; inset: 0;
    display: flex; flex-direction: column; align-items: center; justify-content: center;
    color: var(--brand-red);
    font-weight: 600;
  }
  .back-brand__name { font-size: 44px; letter-spacing: 0.03em; line-height: 1; }
  .back-brand__tag { font-size: 17px; letter-spacing: 0.08em; margin-top: 4px; }
</style>
</head>
<body>
  <section class="card card--front" aria-label="Business card front">
    <div class="brand">
      <span class="brand__dot"></span>
      <div class="brand__name">HARBORLINE<small>SECURITY SYSTEMS INC.</small></div>
    </div>

    <div class="person">
      <p class="person__name">Your Name</p>
      <p class="person__title">Job Title Here</p>
    </div>

    <ul class="contacts">
      <li>
        <svg class="icon" viewBox="0 0 12 12"><path d="M2.5 0.8l2 2-1 1.2a7 7 0 0 0 4.5 4.5l1.2-1 2 2-1.4 1.7C5 11 1 7 0.8 2.2z"/></svg>
        (111) 222 333 444
      </li>
      <li>
        <svg class="icon" viewBox="0 0 12 12"><path d="M3 0h6v12H3z M4 1.5v7.5h4V1.5z"/></svg>
        000 555 0100
      </li>
      <li>
        <svg class="icon" viewBox="0 0 12 12"><path d="M0 2h12v8H0z M0.8 2.6L6 6.6l5.2-4H0.8z" fill-rule="evenodd"/></svg>
        yourmail@email.com
      </li>
    </ul>

    <p class="address">
      <svg class="icon" viewBox="0 0 12 12"><path d="M6 0a4 4 0 0 1 4 4c0 3-4 8-4 8S2 7 2 4a4 4 0 0 1 4-4zm0 2.3a1.7 1.7 0 1 0 0 3.4 1.7 1.7 0 0 0 0-3.4z" fill-rule="evenodd"/></svg>
      1234 address address address
    </p>

    <div class="web-band">
      <svg class="icon" viewBox="0 0 16 16"><circle cx="8" cy="8" r="7" fill="none" stroke="#fff" stroke-width="1.4"/><path d="M1 8h14M8 1c3 3 3 11 0 14M8 1c-3 3-3 11 0 14" fill="none" stroke="#fff" stroke-width="1.2"/></svg>
      www.harborline.com
    </div>
  </section>

  <section class="card card--back" aria-label="Business card back">
    <div class="edge"></div>
    <div class="back-brand">
      <span class="back-brand__name">HARBORLINE</span>
      <span class="back-brand__tag">SECURITY SYSTEMS INC.</span>
    </div>
  </section>
</body>
</html>
```